Chiropractic healthcare group business card

We are a Portland Oregon based chiropractic healthcare group. Looking for a new business card design. Something cutting edge, that shows off our new logo and tag line.Use either of the attached logos.Our tag line = "Who would you be without pain?"I'm open to about anything, impress me!!
Target Market(s)
Chiropractic patients - Auto injury, back pain, sports injuries, neck , shoulder, hip, knee, ankle pain.
Industry/Entity Type
Chiropractic
Contact Information for Business Card
Dr. Bram Holtvick, D.C.
Clinic name - Fernway Chiropractic
2 clinics
location #1
20418 NW Marwick Road
Suite B
North Plains, OR 97133
Location #2
13529 SE Calloway Street
Portland OR 97236
Main phone line 971.555.0143
website : www.FernwayClinics.example
Tag line "Who would you be without pain?"
Colors
Designer to choose colors to be used in the design.
Requirements
Must have
- Use the logo colors -- Want the orange color to be a TRUE orange.
- Both clinic address
- phone number
- website
- personal email - b.holtvick@ReliefBeginsHere.example
- tag line - "Who would you be without pain?"

```html
<!DOCTYPE html>
<html lang="en">
<head>
<meta charset="utf-8">
<title>Fernway Chiropractic – Business Card</title>
<link href="https://fonts.googleapis.com/css2?family=Open+Sans:wght@400;700&family=Poppins:ital,wght@1,800&display=swap" rel="stylesheet">
<style>
  :root {
    --navy: #1b2a66;
    --orange: #e0631f;
    --ink: #333333;
    --text: #3c3c3c;
    --border: #8a8a8a;
    --badge-green: #5aa630;
    --badge-black: #050505;
    --paper: #ffffff;
  }
  * { margin: 0; padding: 0; box-sizing: border-box; }
  html, body { width: 1200px; height: 1200px; overflow: hidden; background: var(--paper); }
  body { position: relative; font-family: "Open Sans", sans-serif; }

  .card {
    position: absolute;
    left: 175px;
    width: 850px;
    height: 520px;
    border: 1px solid var(--border);
    background: var(--paper);
    overflow: hidden;
  }
  .card--front { top: 46px; }
  .card--back { top: 633px; }

  .brand-mark {
    position: absolute;
    display: flex;
    flex-direction: column;
    align-items: center;
    color: var(--navy);
    font-weight: 700;
  }
  .brand-mark__square { background: var(--navy); }
  .card--front .brand-mark { left: 52px; top: 58px; width: 194px; }
  .card--front .brand-mark__square { width: 120px; height: 120px; margin-bottom: 14px; }
  .card--front .brand-mark__name { font-size: 24px; letter-spacing: 0.5px; }
  .card--back .brand-mark { left: 242px; top: 97px; width: 365px; }
  .card--back .brand-mark__square { width: 250px; height: 250px; margin-bottom: 22px; }
  .card--back .brand-mark__name { font-size: 44px; letter-spacing: 1px; }

  .doctor-name {
    position: absolute; left: 316px; top: 52px;
    color: var(--orange); font-size: 25px; font-weight: 700;
  }
  .contact-list { position: absolute; left: 320px; top: 108px; list-style: none; }
  .contact-list li {
    display: flex; align-items: center; height: 36px;
    font-size: 25px; color: var(--text);
  }
  .contact-list svg, .address-list svg { flex: none; fill: var(--orange); }
  .contact-list svg { width: 18px; height: 18px; margin-right: 16px; }

  .clinic-name {
    position: absolute; left: 58px; top: 294px;
    font-size: 26px; font-weight: 700; color: var(--ink);
  }
  .address-list { position: absolute; left: 33px; top: 340px; list-style: none; }
  .address-list li {
    display: flex; align-items: center; height: 30px;
    font-size: 21.5px; color: var(--text);
  }
  .address-list svg { width: 16px; height: 22px; margin-right: 17px; }

  .tagline-band {
    position: absolute; left: 0; top: 452px; width: 100%; height: 51px;
    background: var(--orange);
  }
  .tagline {
    position: absolute; left: 105px; top: 0; line-height: 51px;
    font-family: "Poppins", sans-serif; font-style: italic; font-weight: 800;
    font-size: 27px; color: var(--paper); letter-spacing: 0.3px;
  }
  .partner-badge { position: absolute; top: 444px; width: 67px; height: 66px; }
  .partner-badge--green { left: 691px; background: var(--badge-green); }
  .partner-badge--black { left: 761px; width: 67px; background: var(--badge-black); }
</style>
</head>
<body>

<section class="card card--front">
  <div class="brand-mark">
    <div class="brand-mark__square"></div>
    <div class="brand-mark__name">CRESTLINE CARE</div>
  </div>

  <h1 class="doctor-name">Dr. Bram Holtvick, D.C.</h1>
  <ul class="contact-list">
    <li>
      <svg viewBox="0 0 24 24"><path d="M20 15.5c-1.2 0-2.4-.2-3.6-.6-.3-.1-.7 0-1 .2l-2.2 2.2c-2.8-1.4-5.1-3.8-6.6-6.6l2.2-2.2c.3-.3.4-.7.2-1-.3-1.1-.5-2.3-.5-3.5 0-.6-.4-1-1-1H4c-.6 0-1 .4-1 1 0 9.4 7.6 17 17 17 .6 0 1-.4 1-1v-3.5c0-.6-.4-1-1-1z"/></svg>
      971.555.0143
    </li>
    <li>
      <svg viewBox="0 0 24 24"><path d="M2 5h20v2l-10 6L2 7z"/><path d="M2 9l10 6 10-6v10H2z"/></svg>
      b.holtvick@ReliefBeginsHere.example
    </li>
    <li>
      <svg viewBox="0 0 24 24"><circle cx="12" cy="12" r="10"/><path d="M2 12h20M12 2c3 3 3 17 0 20M12 2c-3 3-3 17 0 20M4 7h16M4 17h16" stroke="#fff" stroke-width="1.3" fill="none"/></svg>
      www.FernwayClinics.example
    </li>
  </ul>

  <h2 class="clinic-name">Fernway Chiropractic</h2>
  <ul class="address-list">
    <li>
      <svg viewBox="0 0 16 22"><path d="M8 0C3.6 0 0 3.5 0 7.8 0 13.6 8 22 8 22s8-8.4 8-14.2C16 3.5 12.4 0 8 0zm0 11a3.2 3.2 0 1 1 0-6.4A3.2 3.2 0 0 1 8 11z"/></svg>
      #1 : 20418 NW Marwick Road, Suite B, North Plains, OR 97133
    </li>
    <li>
      <svg viewBox="0 0 16 22"><path d="M8 0C3.6 0 0 3.5 0 7.8 0 13.6 8 22 8 22s8-8.4 8-14.2C16 3.5 12.4 0 8 0zm0 11a3.2 3.2 0 1 1 0-6.4A3.2 3.2 0 0 1 8 11z"/></svg>
      #2 : 13529 SE Calloway Street, Portland OR 97236
    </li>
  </ul>

  <div class="tagline-band">
    <p class="tagline">Who would you be without pain?</p>
  </div>
  <div class="partner-badge partner-badge--green"></div>
  <div class="partner-badge partner-badge--black"></div>
</section>

<section class="card card--back">
  <div class="brand-mark">
    <div class="brand-mark__square"></div>
    <div class="brand-mark__name">CRESTLINE CARE</div>
  </div>
</section>

</body>
</html>
```